Need an event poster for an automotive event.
The event is a half mile trap speed event. Sometimes called a MaxPace event, they have a 1/2 mile to see how fast They can go. They run one car at a time, it is not a side-by-side race.
Title of the event is “RVLO Sidevalve Autumn Classic”. Dates are October 3-4 2020. Location Blytheville Arkansas. Website is RVLOstretch.com. Most participants will be 50 and older .
All entries must be a carbureted flathead engine .

```html
<!DOCTYPE html>
<html lang="en">
<head>
<meta charset="utf-8">
<title>RVLO Sidevalve Autumn Classic</title>
<link rel="stylesheet" href="https://fonts.googleapis.com/css2?family=Lobster&family=Titan+One&display=swap">
<style>
  :root {
    --cream: #f1e6d5;
    --cream-light: #f6ede0;
    --royal-blue: #3b3fa8;
    --maroon: #8c0a0f;
    --tan-shadow: #c8a57a;
    --teal: #0b4459;
    --brick: #8b332b;
    --white: #ffffff;
  }
  html, body {
    margin: 0;
    padding: 0;
    width: 1200px;
    height: 882px;
    overflow: hidden;
    background: var(--cream);
  }
  .poster {
    position: relative;
    width: 1200px;
    height: 882px;
    overflow: hidden;
    background: var(--cream);
  }
  .poster-art {
    position: absolute;
    inset: 0;
    width: 1200px;
    height: 882px;
  }
  .band-blue, .band-stripe { fill: var(--royal-blue); }
  .band-brick { fill: var(--brick); }
  .car-area { fill: url(#carTones); }
  .brand {
    position: absolute;
    left: 36px;
    top: 96px;
    display: flex;
    align-items: center;
    gap: 10px;
    font-family: "Titan One", sans-serif;
    font-size: 40px;
    line-height: 1;
    color: var(--white);
    letter-spacing: 1px;
  }
  .brand-dot {
    width: 16px;
    height: 16px;
    border-radius: 50%;
    background: var(--white);
  }
  .title-text {
    font-family: "Lobster", cursive;
    paint-order: stroke;
    stroke: var(--cream-light);
    stroke-width: 8px;
    stroke-linejoin: round;
  }
  .title-shadow {
    font-family: "Lobster", cursive;
    fill: var(--tan-shadow);
  }
  .title-line-main { fill: var(--maroon); }
  .title-line-sub { fill: var(--royal-blue); }
  .banner { fill: var(--teal); }
  .banner-text {
    font-family: "Titan One", sans-serif;
    font-size: 28px;
    fill: var(--white);
  }
  .event-info {
    position: absolute;
    left: 396px;
    top: 830px;
    margin: 0;
    font-family: "Titan One", sans-serif;
    font-size: 24px;
    line-height: 1;
    color: var(--white);
    letter-spacing: 1px;
    white-space: nowrap;
  }
  .event-info .dates { font-style: italic; }
  .event-info .divider { margin: 0 10px; }
</style>
</head>
<body>
  <main class="poster">
    <svg class="poster-art" viewBox="0 0 1200 882" xmlns="http://www.w3.org/2000/svg">
      <defs>
        <linearGradient id="carTones" x1="0" y1="0" x2="1" y2="1">
          <stop offset="0" stop-color="#d9583f"/>
          <stop offset="0.6" stop-color="#c9412f"/>
          <stop offset="1" stop-color="#6e2a22"/>
        </linearGradient>
      </defs>

      <polygon class="band-blue" points="0,0 1200,0 1200,48 0,172"/>
      <polygon class="band-stripe" points="0,180 1200,58 1200,64 0,186"/>
      <polygon class="band-stripe" points="0,192 1200,70 1200,76 0,198"/>
      <polygon class="band-stripe" points="0,204 1200,82 1200,88 0,210"/>

      <polygon class="band-brick" points="0,607 1200,824 1200,882 0,882"/>

      <path class="car-area" role="img" aria-label="Illustration of a red vintage roadster with chrome grille and whitewall tyres"
        d="M0,400 L260,400 Q380,430 420,480 Q560,500 600,640 Q615,700 595,730 L440,760 Q330,860 190,865 Q80,868 0,830 Z"/>

      <g transform="rotate(-7 640 280)">
        <text class="title-shadow" x="650" y="300" font-size="140" text-anchor="middle" textLength="1000" lengthAdjust="spacingAndGlyphs">Sidevalve Autumn</text>
        <text class="title-text title-line-main" x="644" y="294" font-size="140" text-anchor="middle" textLength="1000" lengthAdjust="spacingAndGlyphs">Sidevalve Autumn</text>
        <text class="title-shadow" x="690" y="412" font-size="140" text-anchor="middle">Classic</text>
        <text class="title-text title-line-sub" x="684" y="406" font-size="140" text-anchor="middle">Classic</text>
      </g>

      <polygon class="banner" points="600,490 947,437 943,514 596,567"/>
      <text class="banner-text" x="618" y="540" transform="rotate(-8.5 618 540)" textLength="305" lengthAdjust="spacing">TROPHIES AWARDS</text>

      <polygon class="banner" points="596,575 1134,504 1126,571 600,653"/>
      <text class="banner-text" x="618" y="630" transform="rotate(-8 618 630)" textLength="480" lengthAdjust="spacingAndGlyphs">CERTIFIED SPEED CERTIFICATES</text>

      <polygon class="banner" points="616,665 987,614 967,694 616,744"/>
      <text class="banner-text" x="636" y="720" transform="rotate(-8 636 720)" textLength="300" lengthAdjust="spacing">1/2 SPEED TRIALS</text>
    </svg>

    <div class="brand"><span class="brand-dot"></span>RVLO</div>

    <p class="event-info">
      OCT. <span class="dates">3-4, 2020</span><span class="divider">|</span>BLYTHEVILLE, AR<span class="divider">|</span>RVLOSTRETCH.COM
    </p>
  </main>
</body>
</html>
```